New Business Card

We need to refresh our business cards. We designed these ourselves and we have no graphic design experience. We would like to find a new business card design that is professional and unique. We are an auto finance company. Feel free to play with the logo, but we would like to keep the eye very present on the card. Our corporate colors are green, grey, and white.
Green - RGB - 168,215,27; HEX - #AADD22
Grey - RGB - 196,196,196; HEX - #C4C4C4
Need to upload the vector file to finalize the project. The last logo was for a jpeg that didn't stretch well.
Industry/Entity Type
Financial Service
Contact Information for Business Card
Honestly don't know...I need your help!

```html
<!DOCTYPE html>
<html lang="en">
<head>
<meta charset="utf-8">
<title>Brightlane Capital – Business Card</title>
<link href="https://fonts.googleapis.com/css2?family=Signika:wght@300;400;600&display=swap" rel="stylesheet">
<style>
  :root {
    --brand-green: #9bc41c;
    --brand-green-light: #aadd22;
    --brand-grey: #c4c4c4;
    --text-dark: #5b5b5b;
    --text-mid: #6e6e6e;
    --card-face: #f4f5f2;
    --page-bg: #e6e4df;
  }
  * { margin: 0; padding: 0; box-sizing: border-box; }
  html, body {
    width: 1200px; height: 1054px; overflow: hidden;
    background: var(--page-bg);
    font-family: "Signika", sans-serif;
  }
  .card {
    position: absolute; left: 100px; top: 224px;
    width: 1000px; height: 605px;
    background: var(--card-face);
    border-radius: 22px;
    overflow: hidden;
    box-shadow: 0 14px 40px rgba(0,0,0,0.12);
  }
  .brand {
    position: absolute; left: 60px; top: 120px;
    display: flex; align-items: center; gap: 26px;
  }
  .brand-dot {
    width: 92px; height: 92px; border-radius: 50%;
    background: var(--brand-grey);
  }
  .brand-name {
    font-weight: 600; font-size: 58px; line-height: 1;
    color: var(--brand-green); letter-spacing: -0.5px;
  }
  .holder { position: absolute; left: 68px; top: 452px; }
  .holder-name {
    font-weight: 600; font-size: 38px; color: var(--text-dark);
  }
  .holder-title {
    font-weight: 400; font-size: 24px; color: var(--text-mid); margin-top: 6px;
  }
  .contact {
    position: absolute; left: 532px; top: 370px;
    font-weight: 400; font-size: 24px; line-height: 32px; color: var(--text-mid);
  }
  .contact-address { margin-bottom: 14px; }
  .contact-row { display: flex; align-items: center; gap: 22px; }
  .contact-row svg { width: 24px; height: 20px; flex: none; }
  .footer-strip {
    position: absolute; left: 0; bottom: 0; width: 100%; height: 26px;
    background: var(--brand-grey); opacity: 0.55;
  }
  .footer-band {
    position: absolute; right: 0; bottom: 0; width: 570px; height: 74px;
    background: linear-gradient(90deg, var(--brand-green), var(--brand-green-light));
    clip-path: polygon(40px 0, 100% 0, 100% 100%, 0 100%);
  }
  .website {
    position: absolute; left: 532px; bottom: 20px;
    font-weight: 400; font-size: 25px; color: #2f3a10;
  }
</style>
</head>
<body>
  <main class="card">
    <div class="brand">
      <span class="brand-dot"></span>
      <span class="brand-name">Brightlane Capital</span>
    </div>

    <div class="holder">
      <p class="holder-name">Daniel Reyes Moore</p>
      <p class="holder-title">Managing Director</p>
    </div>

    <div class="contact">
      <p class="contact-address">718 Harbor Row, Suite 4,<br>Lakeport, US 402915</p>
      <p class="contact-row">
        <svg viewBox="0 0 24 20" aria-hidden="true"><path fill="#9bc41c" d="M2 6c0-3 4-5 10-5s10 2 10 5v2h-5V6c-1-1-3-1.4-5-1.4S8 5 7 6v2H2zM5 10h14l2 9H3z"/></svg>
        555.014.2287
      </p>
      <p class="contact-row">
        <svg viewBox="0 0 24 20" aria-hidden="true"><path fill="#9bc41c" d="M1 3h22v14H1zM2.5 4.5 12 11l9.5-6.5z"/></svg>
        dmoore@brightlanecapital.com
      </p>
    </div>

    <div class="footer-strip"></div>
    <div class="footer-band"></div>
    <p class="website">www.brightlanecapital.com</p>
  </main>
</body>
</html>
```